Linwell Psychology website transfer from WIX to Wordpress

I have a website currently coded in WIX and I want it (or something like it or better) designed to be coded on Wordpress instead. The website should have mobile optimization so that it can be viewed on mobile devices.

The current website is at: www.linwellpsychology.example

I'm not looking for versions of the website that are very different to what I already have, unless they improve on it aesthetically. I'm mainly looking to have a Wordpress version of this website that I built, away from the WIX ecosystem.
Updates

Need extra days to review

Target Market(s)

Psychology services clients

Coding

Coded - Design and coding required

Number of Pages Required

5+ page

Font styles to use
Serif

Requirements
Must have
• The finished product shoud match my website exactly.
Nice to have
• I'm happy to see new ideas that improve on the current website.
Should not have
• It should not be a different version of my website.

```html
<!DOCTYPE html>
<html lang="en">
<head>
<meta charset="utf-8">
<title>Linwell Psychology</title>
<link href="https://fonts.googleapis.com/css2?family=Open+Sans:wght@300;400;600;700&display=swap" rel="stylesheet">
<style>
:root{
  --navy:#0f1f4b;
  --green:#1e4a3c;
  --green-2:#2b5f4e;
  --sky:#eef7fb;
  --footer:#17344a;
  --text:#6b6f80;
  --orange:#e8891e;
  --line:#d6dbe2;
  --white:#ffffff;
}
*{box-sizing:border-box;margin:0;padding:0}
html,body{width:1200px;height:4320px;overflow:hidden}
body{font-family:"Open Sans",Arial,sans-serif;color:var(--text);background:var(--white);position:relative}
.abs{position:absolute}
/* top bar */
.topbar{left:0;top:0;width:1200px;height:34px;background:#5d6068}
.topbar-shape{left:0;top:0;width:420px;height:34px;background:var(--white);border-bottom-right-radius:60px}
.topbar-info{top:9px;font-size:11px;color:#e9ecef}
.quote-btn{left:846px;top:0;width:108px;height:30px;border-bottom:3px solid #4fa6a0;color:#fff;font-size:11px;text-align:center;line-height:30px}
.nav{left:0;top:34px;width:1200px;height:46px;background:var(--white);border-bottom:1px solid #e4e6ea}
.logo{left:88px;top:26px;font-size:24px;font-weight:300;color:#7a9e98;letter-spacing:1px}
.nav-link{top:51px;font-size:12px;color:#5b6070}
.nav-link.active{color:var(--navy);font-weight:600}
.dot{display:inline-block;width:8px;height:8px;border-radius:50%;background:#cfe3e0;margin-right:4px}
/* hero */
.hero{left:0;top:80px;width:1200px;height:760px;background:linear-gradient(90deg,#0d0f14 0%,#2d3340 32%,#8a8e99 60%,#c9c2bd 100%)}
.hero h1{left:129px;top:262px;width:560px;font-size:44px;line-height:49px;color:#fff;font-weight:600;letter-spacing:.5px}
.hero-copy{left:129px;top:386px;width:450px;font-size:20px;line-height:29px;color:#eef0f3}
.btn-dark{background:var(--green);color:#fff;font-weight:700;font-size:13px;text-align:center;border-radius:22px}
/* who we are */
.sky{left:0;top:830px;width:1200px;height:572px;background:var(--sky)}
.eyebrow{font-size:12px;color:var(--navy);text-transform:uppercase}
.eyebrow-center{left:0;width:1200px;top:870px;text-align:center}
.eyebrow-center span{display:inline-block;padding-bottom:6px;border-bottom:2px solid var(--green)}
.title-xl{font-weight:700;color:var(--navy)}
.center{text-align:center}
.card{background:#fff;box-shadow:0 4px 16px rgba(20,40,70,.08);border-bottom:5px solid var(--green);top:1084px;width:275px;height:240px;text-align:center}
.card h3{position:absolute;left:0;width:100%;font-size:22px;font-weight:600;color:#4b5a6b;letter-spacing:.5px}
.card p{position:absolute;left:36px;width:203px;top:88px;font-size:14px;line-height:21px}
/* about */
.about-text{font-size:12px;line-height:19px;width:455px;left:134px}
.photo{role:img}
/* services strip */
.tab{background:#1d2a55;color:#fff}
.vert{position:absolute;transform:rotate(-90deg);transform-origin:left top;white-space:nowrap;font-size:13px}
/* testimonials */
.testi{left:0;top:2509px;width:1200px;height:645px;background:var(--sky)}
.avatar{border-radius:50%;border:3px solid #fff;box-shadow:0 2px 8px rgba(0,0,0,.15)}
.round-btn{width:44px;height:44px;border-radius:50%;background:var(--green)}
/* contact */
.form-card{left:588px;top:3218px;width:486px;height:545px;background:#fff;border-top:4px solid var(--green);box-shadow:0 4px 20px rgba(20,40,70,.1);border-radius:4px}
.label{font-size:14px;font-weight:700;color:#3c5c8a}
.field{border:1px solid #c9ccd3;font-size:12px;color:#9aa0aa;padding:12px 16px;background:#fff}
.contact-icon{width:36px;height:36px;border-radius:50%;background:#fff;box-shadow:0 2px 8px rgba(0,0,0,.1)}
/* footer */
.foot-head{font-size:15px;font-weight:700;color:#fff}
.foot-text{font-size:12px;line-height:21px;color:#dfe5ec}
.social{width:34px;height:34px;border:1px solid #8ea0b3}
</style>
</head>
<body>

<!-- header -->
<div class="abs topbar"></div>
<div class="abs topbar-shape"></div>
<div class="abs topbar-info" style="left:466px">&#9679; 48 Alder Lane, Brookfield, BF 20418</div>
<div class="abs topbar-info" style="left:705px">Follow Us: <span style="display:inline-block;width:8px;height:8px;background:#e9ecef;margin-left:8px"></span> <span style="display:inline-block;width:8px;height:8px;background:#e9ecef"></span> <span style="display:inline-block;width:8px;height:8px;background:#e9ecef"></span></div>
<div class="abs quote-btn">GET QUOTATION</div>
<div class="abs nav"></div>
<div class="abs logo" style="top:42px"><span class="dot"></span>Linwell Psychology</div>
<div class="abs nav-link active" style="left:404px">Home</div>
<div class="abs nav-link" style="left:484px">Services</div>
<div class="abs nav-link" style="left:566px">About Us</div>
<div class="abs nav-link" style="left:640px">Our Team</div>
<div class="abs nav-link" style="left:716px">And more</div>
<div class="abs nav-link" style="left:790px">Contact Us</div>

<!-- hero -->
<section class="abs hero" role="img" aria-label="Photo of a smiling therapist holding up a sad and a happy face card">
</section>
<h1 class="abs" style="left:129px;top:262px;width:560px;font-size:44px;line-height:49px;color:#fff;font-weight:600">New Perspective for a Better Life</h1>
<p class="abs hero-copy" style="left:129px;top:386px;width:450px;font-size:20px;line-height:29px;color:#eef0f3">Lorem ipsum dolor sit amet, consectetur adipi scing elit, sed do eiusmod tempor incidid unt ut labore et dolore magna aliqua.</p>
<div class="abs btn-dark" style="left:129px;top:501px;width:154px;height:40px;line-height:40px">READ MORE</div>
<svg class="abs" style="left:0;top:600px" width="1200" height="240" viewBox="0 0 1200 240">
  <path d="M1200 20 Q900 160 0 225 L0 240 L1200 240 Z" fill="#eef7fb"/>
  <path d="M0 186 Q480 170 810 136 Q420 205 0 232 Z" fill="#1e4a3c"/>
</svg>

<!-- who we are -->
<section class="abs sky"></section>
<div class="abs eyebrow eyebrow-center"><span>Who we are</span></div>
<h2 class="abs title-xl center" style="left:0;width:1200px;top:904px;font-size:42px">Fostering Mental Clarity</h2>
<p class="abs center" style="left:170px;width:860px;top:975px;font-size:13px;line-height:21px">Lorem ipsum dolor sit amet, consectetur adipiscing elit, sed do eiusmod tempor incididunt ut labore et dolore magna aliqua . Ut enim ad minim veniam, quis laboris nisi ut aliquip ex ea commodo consequat. Lorem ipsum dolor sit am et, consectetur adipiscing elit, sed do eiusmod te a</p>

<div class="abs card" style="left:152px">
  <svg class="abs" style="left:112px;top:62px" width="52" height="58" viewBox="0 0 52 58" fill="none" stroke="#1e4a3c" stroke-width="3" stroke-linecap="round" stroke-linejoin="round">
    <path d="M4 54 H48"/><path d="M10 54 Q10 38 24 36"/><path d="M18 8 L30 4 L36 22 L26 26 Z"/><path d="M28 26 L34 42 L44 46"/><circle cx="22" cy="44" r="4"/>
  </svg>
  <h3 style="top:155px">CLIENT-CENTRIC</h3>
</div>
<div class="abs card" style="left:462px">
  <h3 style="top:36px">PROFESSIONAL</h3>
  <p>Lorem ipsum dolor sit amet, consectetur adipiscing elit, se d do eiusmod tempor incidid unt ut labore et dolore magna ali</p>
</div>
<div class="abs card" style="left:768px">
  <svg class="abs" style="left:106px;top:62px" width="64" height="62" viewBox="0 0 64 62" fill="none" stroke="#1e4a3c" stroke-width="3">
    <path d="M32 6 L58 24 L48 56 L16 56 L6 24 Z"/>
    <circle cx="32" cy="6" r="5" fill="#fff"/><circle cx="58" cy="24" r="5" fill="#fff"/><circle cx="48" cy="56" r="5" fill="#fff"/><circle cx="16" cy="56" r="5" fill="#fff"/><circle cx="6" cy="24" r="5" fill="#fff"/>
  </svg>
  <h3 style="top:155px">EXPERTISE</h3>
</div>

<!-- about -->
<div class="abs eyebrow" style="left:134px;top:1530px;font-size:11px;border-bottom:1px solid var(--navy);padding-bottom:3px">Who we are</div>
<h2 class="abs title-xl" style="left:134px;top:1562px;font-size:37px;line-height:47px;width:500px">Strengthening Minds, Healing Hearts</h2>
<h3 class="abs" style="left:134px;top:1680px;font-size:19px;font-weight:600;color:var(--navy)">Helping You Find Inner Balance</h3>
<p class="abs about-text" style="top:1718px">Lorem ipsum dolor sit amet, consectetur adipiscing elit, sed do eiusmod temp or incididunt ut labore et dolore magna aliqua. Ut enim ad minim veniam, quis laboris nisi ut aliquip ex ea commodo consequat.</p>
<p class="abs about-text" style="top:1787px">Lorem ipsum dolor sit amet, consectetur adipiscing elit, sed do eiusmod temp or incididunt ut labore et dolore magna aliqua.</p>
<div class="abs btn-dark" style="left:134px;top:1852px;width:136px;height:38px;line-height:38px;border-radius:2px">Contact us &nbsp;&#8594;</div>

<div class="abs" style="left:665px;top:1495px;width:430px;height:420px;border-radius:50%;background:#eef0d8"></div>
<div class="abs" role="img" aria-label="Photo of a young man in a flat cap writing in a notebook" style="left:642px;top:1493px;width:426px;height:426px;border-radius:50%;background:linear-gradient(135deg,#8a7466,#b0503f 55%,#5a4a44)"></div>
<div class="abs" role="img" aria-label="Photo of an older man talking during a therapy session" style="left:951px;top:1534px;width:200px;height:200px;border-radius:50%;background:linear-gradient(135deg,#e4ebeb,#b9c7c8 60%,#8d9a97);border:4px solid #fff"></div>
<div class="abs" style="left:651px;top:1820px;width:90px;height:90px;border-radius:50%;background:var(--green);z-index:-0"></div>
<div class="abs" role="img" aria-label="Edge of the young man photo" style="left:642px;top:1493px;width:426px;height:426px;border-radius:50%;clip-path:polygon(0 0,100% 0,100% 100%,30% 100%,30% 80%,0 80%);background:linear-gradient(135deg,#8a7466,#b0503f 55%,#5a4a44)"></div>

<!-- services strip -->
<div class="abs" role="img" aria-label="Photo of hands writing on a clipboard" style="left:0;top:2058px;width:340px;height:451px;background:linear-gradient(135deg,#e9e7e4,#c6c2bd 60%,#8c8580)"></div>
<div class="abs tab" style="left:340px;top:2058px;width:59px;height:451px">
  <div class="vert" style="left:14px;top:400px"><b>&#8594; Psychology Therapy</b></div>
  <div class="vert" style="left:36px;top:400px;font-size:11px;opacity:.85">Lorem ipsum dolor sit amet, consectetu</div>
</div>
<div class="abs" role="img" aria-label="Photo of a smiling father with his young daughter" style="left:399px;top:2058px;width:401px;height:451px;background:linear-gradient(180deg,#c8c0b7 0%,#8a8177 40%,#2a3358 100%)"></div>
<div class="abs" style="left:439px;top:2313px;width:56px;height:56px;border-radius:50%;background:#fff"></div>
<svg class="abs" style="left:451px;top:2324px" width="32" height="34" viewBox="0 0 52 58" fill="none" stroke="#1e2a55" stroke-width="4" stroke-linecap="round"><path d="M4 54 H48"/><path d="M10 54 Q10 38 24 36"/><path d="M18 8 L30 4 L36 22 L26 26 Z"/><circle cx="22" cy="44" r="4"/></svg>
<div class="abs" style="left:439px;top:2381px;font-size:16px;font-weight:700;color:#fff">Clinical Supervision</div>
<p class="abs" style="left:439px;top:2403px;width:330px;font-size:13px;line-height:21px;color:#fff">Lorem ipsum dolor sit amet, consectetur adipiscing elit, sed do eiusmod tempor incididunt ut labore et dolore magna aliqua. Ut enim ad minim</p>
<div class="abs" style="left:439px;top:2470px;font-size:22px;color:#fff">&#10230;</div>
<div class="abs" role="img" aria-label="Photo of a thoughtful young woman in a counselling session" style="left:800px;top:2058px;width:340px;height:451px;background:linear-gradient(135deg,#a45f45,#c79a84 45%,#8b8d92)"></div>
<div class="abs tab" style="left:1140px;top:2058px;width:60px;height:451px">
  <div class="vert" style="left:14px;top:400px"><b>&#8594; Training &amp; Consultancy</b></div>
  <div class="vert" style="left:36px;top:400px;font-size:11px;opacity:.85">Lorem ipsum dolor sit amet, consectetu</div>
</div>

<!-- testimonials -->
<section class="abs testi"></section>
<div class="abs center" style="left:0;width:1200px;top:2574px;font-size:17px;color:var(--navy)">TESTIMONIALS</div>
<h2 class="abs title-xl center" style="left:0;width:1200px;top:2600px;font-size:32px;font-weight:600">What Our Clients are Saying</h2>
<svg class="abs" style="left:0;top:2700px" width="1200" height="220" viewBox="0 0 1200 220">
  <path d="M198 191 Q300 100 382 75 Q500 45 603 40 Q710 45 825 75 Q920 110 1009 191" fill="none" stroke="#3b8ed1" stroke-width="2" stroke-dasharray="6 5"/>
</svg>
<div class="abs avatar" role="img" aria-label="Client portrait" style="left:160px;top:2853px;width:76px;height:76px;background:linear-gradient(135deg,#d9c9bc,#8a7b70)"></div>
<div class="abs avatar" role="img" aria-label="Client portrait" style="left:345px;top:2738px;width:74px;height:74px;background:linear-gradient(135deg,#d7cdc6,#7d6d62)"></div>
<div class="abs avatar" role="img" aria-label="Featured client portrait" style="left:544px;top:2681px;width:118px;height:118px;background:linear-gradient(135deg,#b8c8d8,#5f6f80)"></div>
<div class="abs avatar" role="img" aria-label="Client portrait" style="left:788px;top:2738px;width:74px;height:74px;background:linear-gradient(135deg,#e8e2da,#40495a)"></div>
<div class="abs avatar" role="img" aria-label="Client portrait" style="left:971px;top:2853px;width:76px;height:76px;background:linear-gradient(135deg,#d8d8d8,#8b8a88)"></div>
<svg class="abs" style="left:580px;top:2832px" width="46" height="34" viewBox="0 0 46 34" fill="#1e4a3c"><path d="M0 34 V16 Q0 2 14 0 V7 Q7 9 7 15 H18 V34 Z"/><path d="M26 34 V16 Q26 2 40 0 V7 Q33 9 33 15 H44 V34 Z"/></svg>
<p class="abs center" style="left:290px;width:620px;top:2897px;font-size:18px;line-height:31px;color:#2a2f3a">Lorem ipsum dolor sit amet, consectetur adipiscing elit, sed do eiusmod te dunt ut labore et dolore magna aliqua .dipiscing elit, sed do eiusmod temp dunt ut labore et dolore magna aliqua .dipiscing elit, sed</p>
<div class="abs round-btn" style="left:466px;top:3022px"><svg width="44" height="44" viewBox="0 0 44 44" fill="none" stroke="#fff" stroke-width="2.5"><path d="M30 22 H14 M20 15 L13 22 L20 29"/></svg></div>
<div class="abs round-btn" style="left:697px;top:3022px"><svg width="44" height="44" viewBox="0 0 44 44" fill="none" stroke="#fff" stroke-width="2.5"><path d="M14 22 H30 M24 15 L31 22 L24 29"/></svg></div>
<div class="abs center" style="left:500px;width:206px;top:3005px;font-size:18px;color:var(--orange);letter-spacing:2px">&#9733;&#9733;&#9733;&#9733;&#9733;</div>
<div class="abs center" style="left:500px;width:206px;top:3033px;font-size:19px;font-weight:600;color:var(--orange)">Daniel Mercer</div>
<div class="abs center" style="left:500px;width:206px;top:3064px;font-size:11px;color:#2a2f3a">Client</div>

<!-- contact -->
<h2 class="abs" style="left:140px;top:3276px;font-size:34px;font-weight:600;color:var(--navy);line-height:44px">Get &nbsp;in Touch<br><span style="font-weight:300">Contact Us</span></h2>
<p class="abs" style="left:140px;top:3383px;width:370px;font-size:13px;line-height:21px">Lorem ipsum dolor sit amet, consectetur adipiscing e lit, sed do eiusmod tempor incididunt ut labore et dolore magna aliqua. ceptos ...</p>
<div class="abs" style="left:140px;top:3484px;width:378px;height:1px;background:var(--line)"></div>
<div class="abs contact-icon" style="left:140px;top:3513px"><svg width="36" height="36" viewBox="0 0 36 36"><path d="M18 9 a6 6 0 0 1 6 6 c0 5 -6 11 -6 11 s-6 -6 -6 -11 a6 6 0 0 1 6 -6z" fill="#3b8ed1"/><circle cx="18" cy="15" r="2.2" fill="#fff"/></svg></div>
<div class="abs" style="left:194px;top:3522px;font-size:13px">Hollow Street 9, 3120 Marlow Vale</div>
<div class="abs contact-icon" style="left:140px;top:3575px"><svg width="36" height="36" viewBox="0 0 36 36"><path d="M12 10 l4 0 2 5 -2.5 2 a10 10 0 0 0 4.5 4.5 l2 -2.5 5 2 0 4 a2 2 0 0 1 -2 2 a16 16 0 0 1 -15 -15 a2 2 0 0 1 2 -2z" fill="#3b8ed1"/></svg></div>
<div class="abs" style="left:194px;top:3584px;font-size:13px">+10 555 0148 2290</div>
<div class="abs contact-icon" style="left:140px;top:3631px"><svg width="36" height="36" viewBox="0 0 36 36"><rect x="11" y="13" width="14" height="10" rx="1" fill="#1e3f7a"/><path d="M11 14 L18 19 L25 14" stroke="#fff" stroke-width="1.3" fill="none"/></svg></div>
<div class="abs" style="left:194px;top:3640px;font-size:13px">office@linwell.example</div>

<div class="abs form-card"></div>
<div class="abs label" style="left:624px;top:3266px">Full Name:</div>
<div class="abs field" style="left:618px;top:3297px;width:424px;height:44px">Sed non neque elit.</div>
<div class="abs label" style="left:624px;top:3368px">Email :</div>
<div class="abs label" style="left:850px;top:3368px">Phone no :</div>
<div class="abs field" style="left:618px;top:3400px;width:197px;height:44px">Sed non neque elit.</div>
<div class="abs field" style="left:846px;top:3400px;width:196px;height:44px">Sed non neque elit.</div>
<div class="abs label" style="left:624px;top:3480px">Messages &nbsp;:</div>
<div class="abs field" style="left:618px;top:3511px;width:424px;height:128px">Sed non neque elit.</div>
<div class="abs" style="left:618px;top:3667px;width:126px;height:40px;background:var(--green);border-radius:3px;color:#fff;font-size:13px;font-weight:700;text-align:center;line-height:40px">SUBMIT</div>

<!-- footer -->
<svg class="abs" style="left:0;top:3800px" width="1200" height="520" viewBox="0 0 1200 520">
  <path d="M380 90 Q800 20 1200 10 L1200 40 Q800 50 380 90 Z" fill="#1e4a3c"/>
  <path d="M0 215 Q500 70 1200 40 L1200 520 L0 520 Z" fill="#17344a"/>
</svg>
<div class="abs foot-head" style="left:94px;top:4060px">CONTACT US</div>
<svg class="abs" style="left:92px;top:4103px" width="14" height="18" viewBox="0 0 14 18"><path d="M7 0 a7 7 0 0 1 7 7 c0 5 -7 11 -7 11 s-7 -6 -7 -11 a7 7 0 0 1 7 -7z" fill="#fff"/><circle cx="7" cy="7" r="2.5" fill="#17344a"/></svg>
<div class="abs foot-text" style="left:126px;top:4100px;width:180px">101- lorem ipsum simple text print type text industry text.</div>
<svg class="abs" style="left:92px;top:4159px" width="16" height="16" viewBox="0 0 16 16"><path d="M2 1 l4 0 1.5 4 -2 1.5 a8 8 0 0 0 4 4 l1.5 -2 4 1.5 0 4 a1 1 0 0 1 -1 1 a14 14 0 0 1 -13 -13 a1 1 0 0 1 1 -1z" fill="#fff"/></svg>
<div class="abs foot-text" style="left:126px;top:4156px">555 013 2277</div>
<svg class="abs" style="left:92px;top:4196px" width="18" height="13" viewBox="0 0 18 13"><rect width="18" height="13" fill="#fff"/><path d="M0 1 L9 7 L18 1" stroke="#17344a" stroke-width="1.3" fill="none"/></svg>
<div class="abs foot-text" style="left:126px;top:4192px">info@linwell.example</div>

<div class="abs center" style="left:380px;width:440px;top:4050px;font-size:36px;font-weight:300;color:#fff;letter-spacing:1px">Linwell Psychology</div>
<p class="abs center foot-text" style="left:405px;width:390px;top:4108px">Lorem ipsum dolor sit amet, consectetur adipisc ing elit, sed do eiusmod tempor incididunt bbbbbut bcbbbcbnmx zjzmsmmzm</p>
<div class="abs social" style="left:536px;top:4192px"></div>
<div class="abs social" style="left:580px;top:4192px"></div>
<div class="abs social" style="left:624px;top:4192px"></div>

<div class="abs foot-head" style="left:970px;top:4060px">OPENING HOURS</div>
<div class="abs foot-text" style="right:130px;top:4103px;text-align:right">Mon - Fri: 9am - to - 6pm</div>
<div class="abs foot-text" style="right:130px;top:4134px;text-align:right">Saturday 9am - to - 2pm</div>
<div class="abs foot-text" style="right:130px;top:4165px;text-align:right">Sunday : <u>Closed</u></div>
<svg class="abs" style="left:1088px;top:4106px" width="16" height="80" viewBox="0 0 16 80" fill="none" stroke="#fff" stroke-width="1.4">
  <circle cx="8" cy="8" r="6.5"/><path d="M8 4 V8 H11"/>
  <circle cx="8" cy="39" r="6.5"/><path d="M8 35 V39 H11"/>
  <circle cx="8" cy="70" r="6.5"/><path d="M8 66 V70 H11"/>
</svg>
<div class="abs" style="left:62px;top:4258px;width:1076px;height:1px;background:#3f5a72"></div>
<div class="abs center foot-text" style="left:0;width:1200px;top:4280px">Linwell Psychology</div>

</body>
</html>
```